Book Cover Design KRT

Want a new book cover but want to use the same photo and change the sub name. This is for a brand called "Golden Rose Living". The book is called "Bare Floor, Full Power"

This is for a 8.5 * 11 book size

We really want to brand the Golden Rose Living

I've attached a sample of an old book cover, the photo I want used and the golden rose living logo
Updates

Requirements
Must have
• Must have the logo,

must have the book title. "Bare Floor, Full Power"

Must have "Featuring" The Golden Rose Living Fold Up Card Game"

On the back put the logo and Golden Rose Living Nutrition

must have the authors name "Dana Pellow" on the page

"The Sunrise Shape Guide"
Nice to have
• Golden Rose Living Presents:

the book title

```html
<!DOCTYPE html>
<html lang="en">
<head>
<meta charset="utf-8">
<title>Bare Floor, Full Power — Dana Pellow</title>
<link rel="stylesheet" href="https://fonts.googleapis.com/css2?family=Barlow:wght@300;400;600;700&family=Poppins:wght@100;200;300;800&display=swap">
<style>
  :root {
    --page: #ffffff;
    --ink: #000000;
    --white: #ffffff;
    --logo-grey: #c2c2c2;
    --caption-grey: #a8a8a8;
    --teal: #31a98a;
    --teal-deep: #1c4f57;
    --slate: #5a5a5a;
    --slate-dark: #2a2a2a;
    --yellow: #f5e900;
  }
  * { margin: 0; padding: 0; box-sizing: border-box; }
  html, body {
    width: 848px; height: 1200px; overflow: hidden; background: var(--page);
  }
  .canvas { position: relative; width: 848px; height: 1200px; background: var(--page); }

  .cover {
    position: absolute; left: 111px; top: 204px; width: 626px; height: 813px;
    background: var(--ink); overflow: hidden;
  }
  .band { position: absolute; left: 0; width: 100%; }
  .band--teal {
    top: 367px; height: 174px;
    background: linear-gradient(90deg, var(--teal-deep) 0%, var(--teal) 55%, var(--teal) 100%);
  }
  .band--slate {
    top: 541px; height: 170px;
    background: linear-gradient(200deg, var(--slate-dark) 0%, var(--slate) 45%, var(--slate) 100%);
  }

  .brand-mark {
    position: absolute; right: 24px; top: 62px;
    display: flex; align-items: center; gap: 12px;
    font-family: "Barlow", sans-serif; font-weight: 300;
    font-size: 72px; letter-spacing: 6px; color: var(--logo-grey);
  }
  .brand-mark__square { width: 22px; height: 22px; background: var(--logo-grey); }

  .presents {
    position: absolute; right: 24px; top: 192px;
    font-family: "Barlow", sans-serif; font-weight: 400;
    font-size: 13px; color: var(--caption-grey); letter-spacing: 0.3px;
  }

  .photo {
    position: absolute; left: 0; top: 233px; width: 334px; height: 478px;
    background: linear-gradient(160deg, #2b2b2b 0%, #3d8f7b 45%, #2a2a2a 100%);
    border-radius: 160px 160px 0 0;
    opacity: 0.9;
  }

  .title { position: absolute; right: 24px; top: 210px; text-align: right; z-index: 2; }
  .title__light {
    display: block; font-family: "Poppins", sans-serif; font-weight: 100;
    font-size: 58px; line-height: 1.05; color: var(--white); letter-spacing: -1px;
  }
  .title__bold {
    display: block; font-family: "Barlow", sans-serif; font-weight: 700;
    font-size: 60px; line-height: 1.05; color: var(--white); letter-spacing: 1px;
  }

  .subtitle {
    position: absolute; right: 24px; top: 383px; text-align: right;
    color: var(--yellow); z-index: 2;
  }
  .subtitle__thin {
    display: block; font-family: "Poppins", sans-serif; font-weight: 200;
    font-size: 38px; line-height: 1.05;
  }
  .subtitle__bold {
    display: block; font-family: "Poppins", sans-serif; font-weight: 800;
    font-size: 33px; line-height: 1.15; letter-spacing: -0.5px;
  }

  .feature {
    position: absolute; right: 24px; top: 560px; text-align: right;
    font-family: "Barlow", sans-serif; color: var(--white); z-index: 2;
  }
  .feature__line { display: block; font-size: 26px; line-height: 1.12; font-weight: 300; }
  .feature__line--bold { font-weight: 600; }
  .feature__line--big { font-size: 32px; font-weight: 600; }

  .author {
    position: absolute; right: 30px; top: 733px;
    font-family: "Barlow", sans-serif; font-weight: 300;
    font-size: 30px; color: var(--yellow); letter-spacing: 0.5px;
  }
</style>
</head>
<body>
<div class="canvas">
  <section class="cover">
    <div class="band band--teal"></div>
    <div class="band band--slate"></div>

    <div class="brand-mark"><span class="brand-mark__square"></span>KRT</div>
    <p class="presents">Golden Rose Living Presents</p>

    <div class="photo" role="img" aria-label="Photo of the author in black workout wear, leaning on a green exercise ball"></div>

    <h1 class="title">
      <span class="title__light">BARE FLOOR,</span>
      <span class="title__bold">FULL POWER</span>
    </h1>

    <h2 class="subtitle">
      <span class="subtitle__thin">The</span>
      <span class="subtitle__bold">Sunrise Shape</span>
      <span class="subtitle__thin">Guide</span>
    </h2>

    <p class="feature">
      <span class="feature__line feature__line--bold">"Featuring"</span>
      <span class="feature__line">The Golden Rose</span>
      <span class="feature__line feature__line--big">Living Fold Up</span>
      <span class="feature__line">Card Game"</span>
    </p>

    <p class="author">DANA PELLOW</p>
  </section>
</div>
</body>
</html>
```